Make attractive Packaging label for NUT BUTTERS jars

We at Briarwood Pantry are launching our own line of NUT BUTTERS. We will be serving them in GLASS JARS ready packaged. I need attractive luxurious design for glass jar and should be designed ready to print.
I have attached glass jar pictures and measurement sheet.
My company logo has been attached. Also company details can be found on our facebook page.
product will be

ALMOND BUTTER
CASHEW BUTTER
PEANUT BUTTER
HAZELNUT BUTTER.

Industry/Entity Type

Retail

```html
<!DOCTYPE html>
<html lang="en">
<head>
<meta charset="utf-8">
<title>Briarwood Pantry – Almond Butter Jar Label</title>
<link href="https://fonts.googleapis.com/css2?family=Alfa+Slab+One&family=Hind:wght@400;500;600;700&display=swap" rel="stylesheet">
<style>
  :root {
    --backdrop: #221d02;
    --label-white: #ffffff;
    --band-yellow: #f3b81f;
    --band-yellow-light: #f7c93a;
    --brown-dark: #4a2410;
    --brown-mid: #6b3a14;
    --brown-text: #5a3b24;
    --strip-dash: #b98a12;
    --almond-light: #d9a878;
    --almond-mid: #a8683a;
    --leaf-green: #5f9a2e;
    --organic-green: #5aa83a;
  }
  * { box-sizing: border-box; margin: 0; padding: 0; }
  html, body {
    width: 1200px;
    height: 612px;
    overflow: hidden;
    background: var(--backdrop);
  }
  .canvas {
    position: relative;
    width: 1200px;
    height: 612px;
    background: var(--backdrop);
  }
  .jar-label {
    position: absolute;
    left: 220px;
    top: 136px;
    width: 760px;
    height: 340px;
    background: var(--label-white);
    overflow: hidden;
  }
  .brand-band {
    position: absolute;
    left: 0;
    top: 0;
    width: 150px;
    height: 100%;
    background: linear-gradient(90deg, var(--band-yellow), var(--band-yellow-light));
    border-right: 3px solid var(--brown-mid);
  }
  .brand-name {
    position: absolute;
    left: 14px;
    top: 72px;
    width: 122px;
    display: flex;
    align-items: center;
    gap: 8px;
    font-family: "Hind", sans-serif;
    font-weight: 700;
    font-size: 22px;
    line-height: 1.0;
    color: var(--brown-dark);
  }
  .brand-mark {
    flex: 0 0 12px;
    width: 12px;
    height: 12px;
    background: var(--brown-dark);
  }
  .cert-badges {
    position: absolute;
    left: 22px;
    top: 160px;
    display: flex;
    flex-direction: column;
    gap: 8px;
  }
  .cert-badge {
    width: 38px;
    height: 38px;
    border-radius: 50%;
    border: 2px solid var(--brown-mid);
    background: rgba(255, 255, 255, 0.25);
  }
  .cert-badge--organic {
    width: 46px;
    height: 30px;
    border-radius: 2px;
    border: none;
    background: var(--organic-green);
  }
  .product-photo {
    position: absolute;
    left: 300px;
    top: 18px;
    width: 250px;
    height: 140px;
    border-radius: 40px;
    background: radial-gradient(ellipse at 50% 60%, var(--almond-light) 0%, var(--almond-mid) 55%, rgba(95, 154, 46, 0.35) 80%, rgba(255,255,255,0) 100%);
  }
  .product-title {
    position: absolute;
    left: 185px;
    top: 162px;
    width: 575px;
    font-family: "Alfa Slab One", serif;
    font-size: 40px;
    letter-spacing: 0.5px;
    color: var(--brown-dark);
    white-space: nowrap;
  }
  .product-tagline {
    position: absolute;
    left: 205px;
    top: 210px;
    font-family: "Hind", sans-serif;
    font-weight: 500;
    font-size: 20px;
    color: var(--brown-text);
    letter-spacing: 0.3px;
  }
  .claims-strip {
    position: absolute;
    left: 178px;
    top: 238px;
    width: 582px;
    height: 52px;
    background: var(--band-yellow);
    border-top: 2px dashed var(--strip-dash);
    border-bottom: 2px dashed var(--strip-dash);
    display: flex;
    align-items: center;
    font-family: "Hind", sans-serif;
    color: var(--brown-dark);
  }
  .claim-protein {
    display: flex;
    align-items: center;
    gap: 10px;
    padding-left: 12px;
    width: 170px;
    height: 100%;
    border-right: 2px dashed var(--strip-dash);
  }
  .claim-protein-label {
    font-weight: 600;
    font-size: 18px;
    line-height: 1.05;
  }
  .claim-protein-value {
    font-weight: 500;
    font-size: 26px;
  }
  .claim-natural {
    padding-left: 14px;
    font-weight: 600;
    font-size: 20px;
    letter-spacing: 0.5px;
    white-space: nowrap;
  }
  .texture {
    position: absolute;
    left: 180px;
    top: 302px;
    font-family: "Hind", sans-serif;
    font-weight: 700;
    font-size: 24px;
    letter-spacing: 0.5px;
    color: var(--brown-dark);
  }
  .net-weight {
    position: absolute;
    left: 560px;
    top: 312px;
    font-family: "Hind", sans-serif;
    font-weight: 600;
    font-size: 13px;
    color: var(--brown-dark);
    white-space: nowrap;
  }
</style>
</head>
<body>
<main class="canvas">
  <section class="jar-label">
    <aside class="brand-band">
      <div class="brand-name"><span class="brand-mark"></span><span>Briarwood Pantry</span></div>
      <div class="cert-badges">
        <div class="cert-badge" role="img" aria-label="Gluten free certification badge"></div>
        <div class="cert-badge" role="img" aria-label="GMO free certification badge"></div>
        <div class="cert-badge" role="img" aria-label="100% natural certification badge"></div>
        <div class="cert-badge cert-badge--organic" role="img" aria-label="Organic certification badge"></div>
      </div>
    </aside>

    <div class="product-photo" role="img" aria-label="Photograph of whole almonds in and out of the shell with green leaves"></div>

    <h1 class="product-title">ALMOND BUTTER</h1>
    <p class="product-tagline">RICH SOURCE OF VITAMIN E</p>

    <div class="claims-strip">
      <div class="claim-protein">
        <span class="claim-protein-label">HIGH IN<br>PROTEIN</span>
        <span class="claim-protein-value">21%</span>
      </div>
      <span class="claim-natural">ALL NATURAL</span>
    </div>

    <p class="texture">SMOOTH</p>
    <p class="net-weight">NET WT. 12 OZ (340g)</p>
  </section>
</main>
</body>
</html>
```